This is book 2 to Quarry Lantern. I'm looking for something that feels similar, with the same cymatic image used on Antarctica on the first book cover (see the cover image attached; the original designer said this was the image used: https://www.filebarrow.net/s/k7vq2m9xp4tl/cymatic-image.png). Differences: the cover should be all black (no Antarctica, no globe, nothing but the image), the cymatic image kind of a pale grayish white (subtle, not calling too much attention to itself. Think the subtle dragon on "The Boy Beneath the Copper Moon"--like that sort of). Same font as before, but red this time (with the color progression like in the first one, only red instead of blue), with the title (Quarry Tempest), author name (J.L. Pome), and subtitle (Fall of the Veshtari, Book 2)

Target Market(s)

adult action/adventure and thriller readers

Industry/Entity Type

media and literature

Colors
EB3D1F
EC4F4E
F09395
F8D3D4
FCEDEE

Requirements
Must have
• look like part of the series before
Should not have
• not too busy

```html
<!DOCTYPE html>
<html lang="en">
<head>
<meta charset="utf-8">
<title>Quarry Tempest — Fall of the Veshtari, Book 2</title>
<link rel="stylesheet" href="https://fonts.googleapis.com/css2?family=Bebas+Neue&family=Cinzel:wght@400;600&display=swap">
<style>
  :root {
    --backdrop: #dcdcdc;
    --space: #0b0b12;
    --glow: #a8262a;
    --red-deep: #7e161b;
    --red-bright: #e61b22;
    --red-sub: #d31c24;
    --flare: #ff5a5a;
    --white: #ffffff;
    --pale: #c9ccd2;
  }
  * { margin: 0; padding: 0; box-sizing: border-box; }
  html, body { width: 1200px; height: 1200px; overflow: hidden; background: var(--backdrop); }
  .cover {
    position: absolute; left: 217px; top: 26px; width: 765px; height: 1148px;
    overflow: hidden;
    background:
      radial-gradient(ellipse 70% 14% at 50% 0%, var(--glow) 0%, rgba(168,38,42,0.35) 45%, transparent 100%),
      radial-gradient(circle at 12% 22%, rgba(255,255,255,.8) 0 1px, transparent 2px),
      radial-gradient(circle at 78% 9%, rgba(255,255,255,.7) 0 1px, transparent 2px),
      radial-gradient(circle at 35% 66%, rgba(255,255,255,.7) 0 1px, transparent 2px),
      radial-gradient(circle at 8% 80%, rgba(255,255,255,.6) 0 1px, transparent 2px),
      radial-gradient(circle at 92% 52%, rgba(255,255,255,.7) 0 1px, transparent 2px),
      radial-gradient(circle at 55% 35%, rgba(255,255,255,.6) 0 1px, transparent 2px),
      var(--space);
  }
  .cymatic {
    position: absolute; left: 119px; top: 496px; width: 744px; height: 744px;
  }
  .title {
    position: absolute; left: 0; width: 100%; text-align: center;
    font-family: "Bebas Neue", "Oswald", sans-serif;
    font-size: 238px; line-height: 1; letter-spacing: 2px;
    background: linear-gradient(180deg, var(--red-deep) 8%, var(--red-bright) 45%, var(--red-bright) 62%, var(--red-deep) 95%);
    -webkit-background-clip: text; background-clip: text; color: transparent;
  }
  .title-first { top: 70px; }
  .title-second { top: 262px; }
  .series-band {
    position: absolute; left: 0; top: 466px; width: 100%; height: 78px;
    background: linear-gradient(180deg, transparent, rgba(90,8,10,.55) 30%, rgba(90,8,10,.55) 70%, transparent);
  }
  .flare {
    position: absolute; left: 0; width: 100%; height: 3px;
    background: linear-gradient(90deg, transparent, var(--red-bright) 15%, var(--flare) 50%, var(--red-bright) 85%, transparent);
    box-shadow: 0 0 10px 2px rgba(230,27,34,.7);
  }
  .flare-top { top: 12px; }
  .flare-bottom { top: 64px; }
  .series {
    position: absolute; left: 0; top: 22px; width: 100%; text-align: center;
    font-family: "Cinzel", serif; font-weight: 600; font-size: 27px; letter-spacing: 1px;
    color: var(--red-sub);
  }
  .author {
    position: absolute; left: 82px; top: 1024px;
    font-family: "Cinzel", serif; font-weight: 400; font-size: 34px; letter-spacing: 1px;
    color: var(--white);
  }
</style>
</head>
<body>
  <main class="cover">
    <svg class="cymatic" viewBox="0 0 744 744" role="img" aria-label="Pale grayish-white cymatic sound-wave pattern, a circular radiating form">
      <defs>
        <radialGradient id="cymatic-tone" cx="50%" cy="50%" r="50%">
          <stop offset="0%" stop-color="#8d9098" stop-opacity=".55"/>
          <stop offset="55%" stop-color="#4a4d56" stop-opacity=".45"/>
          <stop offset="88%" stop-color="#9a9ca4" stop-opacity=".5"/>
          <stop offset="100%" stop-color="#0b0b12" stop-opacity="0"/>
        </radialGradient>
      </defs>
      <circle cx="372" cy="372" r="372" fill="url(#cymatic-tone)"/>
    </svg>

    <h1 class="title-wrap">
      <span class="title title-first">QUARRY</span>
      <span class="title title-second">TEMPEST</span>
    </h1>

    <div class="series-band">
      <div class="flare flare-top"></div>
      <p class="series">FALL OF THE VESHTARI, BOOK 2</p>
      <div class="flare flare-bottom"></div>
    </div>

    <p class="author">J.L. POME</p>
  </main>
</body>
</html>
```